Brightmoor Partners Branding Revamp

We are a consulting company, looking for a way to display and promote our brand. We have 2 sides to the business- Brightmoor (financial) and Partners (cyber security). The financial side products relate to business necessities: card processing, website design/hosting/maintenance, VoIP phone systems. The cyber security side promotes a bundled package of 4 solutions: network vulnerability scan, dark web scan, anti-ransomeware/malware software, and image-level backups. We want people to understand that partnering with Brightmoor Partners gives them “Elevated Peace of Mind” (tagline). Current badge and logos uploaded.

Target Market(s)

Small businesses

Contact Information for Business Card

Lena Marwick, Vice President, lena@brightmoorpartners.example, 555-806-1937, www.brightmoorpartners.example

Requirements
Nice to have
• I do prefer the darker background for front and back

```html
<!DOCTYPE html>
<html lang="en">
<head>
<meta charset="utf-8">
<title>Brightmoor Partners – Business Card</title>
<link rel="stylesheet" href="https://fonts.googleapis.com/css2?family=Roboto:wght@400;500&display=swap">
<style>
  :root {
    --backdrop: #d3d3d3;
    --card: #1e1e1e;
    --card-glow: #272727;
    --accent: #e0302a;
    --ink: #f2f2f2;
  }
  * { margin: 0; padding: 0; box-sizing: border-box; }
  html, body {
    width: 1200px;
    height: 800px;
    overflow: hidden;
    background: var(--backdrop);
    font-family: "Roboto", Arial, sans-serif;
  }
  .canvas {
    position: relative;
    width: 1200px;
    height: 800px;
  }
  .card {
    position: absolute;
    top: 284px;
    width: 429px;
    height: 237px;
    background: radial-gradient(ellipse at 40% 30%, var(--card-glow) 0%, var(--card) 70%);
    color: var(--ink);
  }
  .card--front { left: 111px; }
  .card--back { left: 638px; }

  .person {
    position: absolute;
    left: 27px;
    top: 115px;
  }
  .person__name {
    color: var(--accent);
    font-size: 16.5px;
    font-weight: 400;
    line-height: 1.1;
  }
  .person__title {
    font-size: 11.5px;
    font-weight: 400;
    margin-top: 3px;
  }

  .contact {
    position: absolute;
    left: 26px;
    top: 171px;
    list-style: none;
  }
  .contact__item {
    display: flex;
    align-items: center;
    gap: 4px;
    font-size: 11.5px;
    letter-spacing: 0.4px;
    height: 17px;
  }
  .contact__icon {
    width: 11px;
    height: 11px;
    fill: var(--accent);
    flex: none;
  }

  .brand-mark {
    position: absolute;
    display: flex;
    align-items: center;
    gap: 7px;
    font-weight: 500;
  }
  .brand-mark__square {
    background: var(--accent);
    flex: none;
  }
  .card--front .brand-mark {
    right: 24px;
    bottom: 28px;
    color: var(--accent);
    font-size: 14px;
  }
  .card--front .brand-mark__square { width: 10px; height: 10px; }

  .card--back .brand-mark {
    left: 50%;
    top: 50%;
    transform: translate(-50%, -50%);
    color: var(--ink);
    font-size: 24px;
    letter-spacing: 3px;
    text-transform: uppercase;
    white-space: nowrap;
  }
  .card--back .brand-mark__square { width: 16px; height: 16px; }
</style>
</head>
<body>
<main class="canvas">
  <section class="card card--front" aria-label="Business card front">
    <div class="person">
      <h1 class="person__name">LENA MARWICK</h1>
      <p class="person__title">VICE PRESIDENT</p>
    </div>
    <ul class="contact">
      <li class="contact__item">
        <svg class="contact__icon" viewBox="0 0 12 12" aria-hidden="true"><path d="M0 2h12v8H0z M1 3l5 4 5-4" fill="var(--accent)"/><path d="M1 3l5 4 5-4" fill="none" stroke="#1e1e1e" stroke-width="1"/></svg>
        lena@brightmoorpartners.example
      </li>
      <li class="contact__item">
        <svg class="contact__icon" viewBox="0 0 12 12" aria-hidden="true"><path d="M2.5 0.8l2 2.2-1 1.5c.8 1.7 2 2.9 3.8 3.8l1.5-1 2.2 2-1.4 1.9C5 10.8 1.2 7 .6 2.2z"/></svg>
        555-806-1937
      </li>
      <li class="contact__item">
        <svg class="contact__icon" viewBox="0 0 12 12" aria-hidden="true"><g fill="none" stroke="var(--accent)" stroke-width="1"><circle cx="6" cy="6" r="5.3"/><ellipse cx="6" cy="6" rx="2.3" ry="5.3"/><path d="M.7 6h10.6M1.6 3.3h8.8M1.6 8.7h8.8"/></g></svg>
        www.brightmoorpartners.example
      </li>
    </ul>
    <div class="brand-mark">
      <span class="brand-mark__square" aria-hidden="true"></span>
      <span class="brand-mark__name">Brightmoor Partners</span>
    </div>
  </section>

  <section class="card card--back" aria-label="Business card back">
    <div class="brand-mark">
      <span class="brand-mark__square" aria-hidden="true"></span>
      <span class="brand-mark__name">Brightmoor Partners</span>
    </div>
  </section>
</main>
</body>
</html>
```